Harlow Ironworks Business Card

We need a business card design for a new small metal fabrication business in rural NSW, Australia.

The business (Harlow Ironworks) is owner operated by a man with the initials KB - much of the branding comes from this name.

Harlow Ironworks designs, engineers, repairs and manufactures a range of custom, quality metal works including vehicle trays, agricultural machinery impliments, trailers, wood splitters, fire pits, furniture etc.

The brand position focuses on custom work of the highest quality.

Business card design should show quality, attention to detail and stand out among a mass of business cards.

Logos are in the files

The grey color may be changed on the logo if required to stand out more.

There is an image attached of a simple card that is liked because it is clean, clear, simple, masculine and effective. It says 'quality'. As most of the work we do is custom it would be good to have the business card speak to this.

Target Market(s)

Rural and regional based Australians. Primarily adult male 25-60 yrs. Primary production / rural / travelling lifestyle.

Industry/Entity Type

Metal Fabrication

Contact Information for Business Card

The words 'custom quality fabrications' would be great somewhere perhaps on the backside (not on the information side)
Name
title
Phone: 0418 539 746 and (02) 6193 4827
email: info@harlowiw.com.au
www.harlowiw.com.au

address (2 lines)

Requirements
Nice to have
• Background colour should be very navy blue or black.
Should not have
• NO orange and blue combinations.
• Navy is OK

```html
<!DOCTYPE html>
<html lang="en">
<head>
<meta charset="utf-8">
<title>Harlow Ironworks Business Card</title>
<link rel="stylesheet" href="https://fonts.googleapis.com/css2?family=Arimo:wght@400&family=Open+Sans:wght@400;700;800&display=swap">
<style>
  :root {
    --page: #e9e7e4;
    --navy: #0a0f8c;
    --navy-deep: #050868;
    --black: #050505;
    --charcoal: #141414;
    --green: #5fd33a;
    --white: #ffffff;
    --steel-light: #eeeeee;
    --steel-dark: #3a3a3a;
  }
  * { box-sizing: border-box; margin: 0; padding: 0; }
  html, body { width: 1200px; height: 754px; overflow: hidden; }
  body {
    background: var(--page);
    display: flex;
    align-items: center;
    justify-content: center;
    gap: 40px;
    font-family: "Open Sans", sans-serif;
  }
  .card {
    position: relative;
    width: 540px;
    height: 330px;
    overflow: hidden;
    box-shadow: 0 6px 18px rgba(0,0,0,.25);
  }

  /* ---------- information side ---------- */
  .card-front {
    background: radial-gradient(ellipse at 60% 45%, var(--charcoal), var(--black) 75%);
    color: var(--white);
  }
  .brand {
    position: absolute;
    top: 34px;
    left: 34px;
    display: flex;
    align-items: center;
    gap: 12px;
  }
  .brand-mark {
    width: 30px;
    height: 30px;
    background: var(--green);
  }
  .brand-name {
    font-weight: 800;
    font-size: 30px;
    letter-spacing: 1px;
    color: var(--white);
    text-transform: uppercase;
  }
  .contact {
    position: absolute;
    left: 34px;
    font-family: "Arimo", sans-serif;
    font-size: 14px;
    line-height: 19px;
    display: flex;
    align-items: flex-start;
    gap: 8px;
  }
  .contact-icons {
    display: flex;
    flex-direction: column;
    gap: 4px;
    padding-top: 2px;
  }
  .contact-rule {
    width: 2px;
    background: var(--green);
    align-self: stretch;
  }
  .contact-phone { top: 112px; }
  .contact-address { top: 168px; }
  .person {
    position: absolute;
    right: 40px;
    top: 150px;
    text-align: right;
  }
  .person-name {
    font-weight: 700;
    font-size: 20px;
    color: var(--green);
    text-transform: uppercase;
    padding-bottom: 3px;
    border-bottom: 1px solid #777;
  }
  .person-role {
    font-size: 12px;
    margin-top: 3px;
    padding-right: 60px;
  }
  .band {
    position: absolute;
    left: 0;
    right: 0;
    background: var(--navy);
    border-top: 4px solid var(--white);
    box-shadow: 0 -6px 0 var(--navy);
  }
  .band-front {
    bottom: 14px;
    height: 92px;
    display: flex;
    align-items: flex-end;
    justify-content: flex-end;
    padding: 0 24px 10px;
  }
  .band-front::after,
  .band-back::after {
    content: "";
    position: absolute;
    left: 0; right: 0; bottom: -10px;
    height: 6px;
    background: var(--white);
  }
  .web {
    font-weight: 700;
    font-size: 16px;
    letter-spacing: 2px;
    color: var(--white);
  }

  /* ---------- tagline side ---------- */
  .card-back { background: var(--navy-deep); }
  .emblem {
    position: absolute;
    left: 50%;
    top: -20px;
    width: 300px;
    height: 300px;
    transform: translateX(-50%);
    border-radius: 50%;
    background: radial-gradient(circle, var(--navy) 0 62%, var(--steel-light) 64%, var(--steel-dark) 80%, var(--black) 100%);
  }
  .back-brand {
    position: absolute;
    left: 0; right: 0;
    top: 118px;
    text-align: center;
    font-weight: 800;
    font-size: 30px;
    letter-spacing: 1px;
    color: var(--white);
    text-transform: uppercase;
  }
  .band-back {
    bottom: 14px;
    height: 60px;
    display: flex;
    align-items: center;
    justify-content: center;
  }
  .tagline {
    font-weight: 700;
    font-size: 15px;
    letter-spacing: 1px;
    color: var(--white);
  }
</style>
</head>
<body>

  <section class="card card-front" aria-label="Business card, information side">
    <div class="brand">
      <span class="brand-mark"></span>
      <span class="brand-name">Harlow Ironworks</span>
    </div>

    <div class="contact contact-phone">
      <div class="contact-icons">
        <svg width="14" height="14" viewBox="0 0 24 24" aria-hidden="true"><path fill="#5fd33a" d="M6.6 10.8a15 15 0 0 0 6.6 6.6l2.2-2.2a1 1 0 0 1 1-.25 11.4 11.4 0 0 0 3.6.57 1 1 0 0 1 1 1V20a1 1 0 0 1-1 1A17 17 0 0 1 3 4a1 1 0 0 1 1-1h3.5a1 1 0 0 1 1 1c0 1.25.2 2.45.57 3.57a1 1 0 0 1-.25 1z"/></svg>
        <svg width="14" height="12" viewBox="0 0 24 18" aria-hidden="true"><rect x="1" y="1" width="22" height="16" fill="#5fd33a"/><path d="M1 1l11 9 11-9" fill="none" stroke="#050505" stroke-width="2"/></svg>
      </div>
      <span class="contact-rule"></span>
      <div>
        <p>0418 539 746 / (02) 6193 4827</p>
        <p>info@harlowiw.com.au</p>
      </div>
    </div>

    <div class="contact contact-address">
      <div class="contact-icons">
        <svg width="14" height="14" viewBox="0 0 24 24" aria-hidden="true"><path fill="#5fd33a" d="M12 3l10 9h-3v9h-5v-6h-4v6H5v-9H2z"/></svg>
      </div>
      <span class="contact-rule"></span>
      <div>
        <p>House Number Street City estate</p>
        <p>House Number Street City estate</p>
      </div>
    </div>

    <div class="person">
      <p class="person-name">Name Surname</p>
      <p class="person-role">Position</p>
    </div>

    <div class="band band-front">
      <span class="web">www.harlowiw.com.au</span>
    </div>
  </section>

  <section class="card card-back" aria-label="Business card, tagline side">
    <div class="emblem" role="img" aria-label="Steel gear emblem framing the business name"></div>
    <p class="back-brand">Harlow Ironworks</p>
    <div class="band band-back">
      <span class="tagline">Custom Quality Fabrications</span>
    </div>
  </section>

</body>
</html>
```